A Speech Therapy Business needs to update their logo

I need an update to the font and color of my logo to look more appealing. I am looking to open a private practice as a Speech Language Pathologist that caters to adults and children. It needs to be sophisticated and friendly at the same time. I want to keep the silhouette in my logo as is, just update the font and color for "Brightpaths".
Industry/Entity Type
Business
Contact Information for Business Card
I want the business card to have my logo, my name (Dorota Valk, CCC-SLP, TSSLD) and that I am a Bilingual Speech Language Pathologist. Also, include my phone number, (555) 271-8390. Include my website, Brightpathsslp.example, and email address, dorotavalk@brightpathsslp.example
Look and feel
Each slider illustrates characteristics of the customer's brand and the style your logo design should communicate.

```html
<!DOCTYPE html>
<html lang="en">
<head>
<meta charset="utf-8">
<title>Brightpaths Business Card</title>
<link rel="stylesheet" href="https://fonts.googleapis.com/css2?family=Open+Sans:wght@400;600;700&display=swap">
<style>
  :root {
    --stage: #1f1f1f;
    --card-dark: #000000;
    --brand-purple: #7b5fac;
    --brand-purple-deep: #7256a3;
    --ink-light: #ffffff;
  }
  * { margin: 0; padding: 0; box-sizing: border-box; }
  html, body {
    width: 1200px; height: 900px; overflow: hidden;
    background: var(--stage);
    font-family: "Open Sans", Arial, sans-serif;
  }
  .stage { position: relative; width: 1200px; height: 900px; }
  .card {
    position: absolute; top: 170px;
    width: 347px; height: 561px;
    overflow: hidden;
  }
  .card--front { left: 259px; background: var(--card-dark); }
  .card--back { left: 631px; background: var(--brand-purple); }

  .accent-bar {
    position: absolute; left: 102px;
    width: 143px; height: 30px;
    background: var(--brand-purple);
  }
  .accent-bar--top { top: 0; }
  .accent-bar--bottom { bottom: 0; height: 28px; }

  .family-silhouette {
    position: absolute;
    background: linear-gradient(90deg, rgba(255,255,255,0.92), rgba(255,255,255,0.78));
    clip-path: polygon(0 0, 12% 0, 100% 78%, 100% 100%, 0 100%);
  }
  .card--front .family-silhouette { left: 55px; top: 112px; width: 265px; height: 100px; }
  .card--back .family-silhouette { left: 29px; top: 178px; width: 285px; height: 118px; }

  .backdrop-figures {
    position: absolute; left: 30px; top: 50px; width: 317px; height: 430px;
    background: radial-gradient(ellipse at 45% 50%, var(--brand-purple-deep) 0%, var(--brand-purple) 70%);
    opacity: 0.8;
  }

  .brand-name {
    position: absolute; left: 0; width: 100%;
    text-align: center;
    font-weight: 400;
    letter-spacing: 1px;
    line-height: 1;
  }
  .card--front .brand-name { top: 232px; font-size: 50px; color: var(--brand-purple); }
  .card--back .brand-name { top: 304px; font-size: 56px; color: var(--ink-light); }

  .contact {
    position: absolute; left: 0; top: 366px; width: 100%;
    text-align: center; color: var(--ink-light);
  }
  .contact__name {
    font-size: 17px; font-weight: 700; color: var(--brand-purple);
    text-transform: uppercase; letter-spacing: 0.3px;
  }
  .contact__credentials { font-size: 14px; font-weight: 400; }
  .contact__title { font-size: 14px; margin-top: 2px; }
  .contact__lines { margin-top: 31px; font-size: 14px; line-height: 20px; }
  .contact__label { color: var(--brand-purple); font-weight: 600; }
  .contact__web { color: var(--brand-purple); }
</style>
</head>
<body>
<main class="stage">
  <section class="card card--front">
    <div class="accent-bar accent-bar--top"></div>
    <div class="family-silhouette" role="img" aria-label="Silhouette of a family row, from adult to baby, holding hands"></div>
    <div class="brand-name">Brightpaths</div>
    <div class="contact">
      <p class="contact__name">Dorota Valk,<span class="contact__credentials">CCC-SLP, TSSLD</span></p>
      <p class="contact__title">Bilingual Speech Language Pathologist</p>
      <div class="contact__lines">
        <p><span class="contact__label">P:</span> (555) 271-8390</p>
        <p><span class="contact__label">E:</span> dorotavalk@brightpathsslp.example</p>
        <p class="contact__web">www.Brightpathsslp.example</p>
      </div>
    </div>
    <div class="accent-bar accent-bar--bottom"></div>
  </section>

  <section class="card card--back">
    <div class="backdrop-figures" role="img" aria-label="Large faint embossed family silhouettes in the background"></div>
    <div class="family-silhouette" role="img" aria-label="Silhouette of a family row, from adult to baby, holding hands"></div>
    <div class="brand-name">Brightpaths</div>
  </section>
</main>
</body>
</html>
```